Business card and stationary for consulting business

We need business cards and matching stationary for professional consulting business for employment and human resources issues.
One of the CraftHive designers designed the logo with our company name.  Use the colors in the logo and may use light yellow as an accent color.
Add
Mara T. Vollen, J.D., LL.M.
485 E. Callister Lane
Winter Park, Florida  32789
407-555-0183
maravollenjd@quillpost.example

Industry/Entity Type
Business

```html
<!DOCTYPE html>
<html lang="en">
<head>
<meta charset="utf-8">
<title>Kestrel People – Business Card, Front and Back</title>
<link rel="stylesheet" href="https://fonts.googleapis.com/css2?family=Nunito+Sans:wght@400;600;800&family=Arimo:wght@400;700&display=swap">
<style>
  :root {
    --backdrop: #e9e6e1;
    --paper: #ffffff;
    --brand-teal: #186b8a;
    --brand-blue: #1f6f98;
    --tagline: #2c7aa3;
    --rule: #9bb6c4;
    --ink-light: #ffffff;
  }
  * { margin: 0; padding: 0; box-sizing: border-box; }
  html, body {
    width: 1200px;
    height: 927px;
    overflow: hidden;
    background: var(--backdrop);
  }
  .sheet {
    position: relative;
    width: 1200px;
    height: 927px;
  }
  .card {
    position: absolute;
    top: 190px;
    width: 409px;
    height: 245px;
    overflow: hidden;
    box-shadow: 0 2px 6px rgba(0,0,0,0.12);
  }
  .card--front { left: 143px; background: var(--paper); }
  .card--back { left: 612px; background: var(--brand-teal); }

  .lockup {
    position: absolute;
    inset: 0;
    display: flex;
    align-items: center;
    justify-content: center;
    gap: 8px;
  }
  .lockup__name {
    font-family: "Nunito Sans", sans-serif;
    font-weight: 600;
    font-size: 24px;
    color: var(--brand-blue);
  }
  .lockup__rule {
    width: 1px;
    height: 52px;
    background: var(--rule);
  }
  .tagline {
    list-style: none;
    font-family: "Nunito Sans", sans-serif;
    font-weight: 400;
    font-size: 11px;
    line-height: 13.5px;
    color: var(--tagline);
  }

  .contact {
    position: absolute;
    right: 28px;
    top: 120px;
    text-align: right;
    font-family: "Arimo", sans-serif;
    color: var(--ink-light);
    font-size: 12.5px;
    line-height: 16px;
  }
  .contact__name {
    font-weight: 700;
    font-size: 13px;
    margin-bottom: 6px;
  }
  .contact__address { font-style: normal; margin-bottom: 4px; }
  .wordmark-large {
    position: absolute;
    left: 12px;
    bottom: 10px;
    font-family: "Nunito Sans", sans-serif;
    font-weight: 800;
    font-size: 44px;
    line-height: 1;
    color: var(--ink-light);
  }
</style>
</head>
<body>
  <main class="sheet">
    <section class="card card--front" aria-label="Business card front">
      <div class="lockup">
        <span class="lockup__name">Kestrel People</span>
        <span class="lockup__rule"></span>
        <ul class="tagline">
          <li>Grow Revenue</li>
          <li>Control Expenses</li>
          <li>Guard Margins</li>
        </ul>
      </div>
    </section>

    <section class="card card--back" aria-label="Business card back">
      <div class="contact">
        <p class="contact__name">Mara T. Vollen, J.D., LL.M.</p>
        <address class="contact__address">
          485 E. Callister Lane,<br>
          Alder Bay, Florida 32961
        </address>
        <p>407-555-0183</p>
        <p>maravollenjd@quillpost.example</p>
      </div>
      <span class="wordmark-large">Kestrel</span>
    </section>
  </main>
</body>
</html>
```